Flyer needed to promote gutter clearance service for established gardening company

We need a bright and engaging flyer to be designed to advertise our gutter clearance service.
Whilst we are a gardening company that normally does more horticultural work, during the winter we offer other services such as gutter clearance where we remove the debris from gutters and thereby reducing the risk of clogs, leakage, breakage and potential structural damage to the property.

Full details of our service, together with our overall brand and colours can be seen on www.marlowtreecare.co.uk/gutters.

We would like you to use the page on the website as a basis to create the flyer and so please feel free to use as much or as little of the wording contained within the webpage on the flyer drawing particular attention to "Prices starting at just £60 for an average 3 bed house". I will upload pictures but please feel free to use other graphics and fonts to make it stand out.

The contact details which should be included within the flyer are as follows:

Marlow Treecare Services Ltd
Orbit Trading Centre
Fairbrook Vale Ind Estate
Swindon
SN4 7HW

Tel: 01793 418302
www.marlowtreecare.co.uk
dean@marlowtreecare.co.uk

The flyers will eventually be printed out in A5 (210mm x 148mm) using Printelle and so needs to be in that size and suitable file for upload.

I have only put this as a 2 day project as its really urgent and I'm hoping we get some great designs in that time.

Target Market(s)

Homeowners between 25 - 65+

Industry/Entity Type

Home Improvement

Font styles to use
Serif
Sans Serif
Decorative
Script

Colors
6b449b
9bcb3c

Requirements
Must have
• Our colours are purple and green as seen on our website www.marlowtreecare.co.uk/gutters. Please use those colours.
• The flyer should draw attention to the following facts:
• We are Marlow Treecare Services Ltd (see attached logo)
• We are offering a Gutter Clearance Service in Swindon
• Prices start at just £60 for the average 3 bed house.
• We are fully insured.
• Our contact details must be included (as in the product description above)
• I have attached pictures but feel free to add other graphics or use fonts to make the flyer more engaging and interesting.
• Additional wording may be taken from the website at the address shown above. You can use as much or as little wording as you like just as long as the message gets across and the flyer contains our contact information and logo and the details shown above.
Nice to have
• I would like a bright and modern design which isn't too busy or cluttered. It should be something that is quick and easy to read.
Should not have
• I don't want it to look too busy or crowded with small type which people just won't read. Whilst I've said you can take whatever wording you want from our website, I'd suggest you don't take it all or too much. I want the main message (as detailed above in 'must haves') to stand out rather than have it contained deep within lots of small type face.

```html
<!DOCTYPE html>
<html lang="en">
<head>
<meta charset="utf-8">
<title>Marlow Treecare – Gutter Clearance Flyer</title>
<link rel="stylesheet" href="https://fonts.googleapis.com/css2?family=Elsie:wght@900&family=Raleway:wght@400;500;600;800&display=swap">
<style>
  :root{
    --cream:#f2efe5;
    --paper:#fbfaf5;
    --purple:#8b2a7e;
    --purple-light:#a8388f;
    --green:#43a83a;
    --green-light:#9bcb3c;
    --green-dark:#2f8f2e;
    --ink:#444444;
    --silver:#e3e3e3;
  }
  *{margin:0;padding:0;box-sizing:border-box}
  html,body{width:846px;height:1200px;overflow:hidden;background:var(--cream)}
  .flyer{position:relative;width:846px;height:1200px;overflow:hidden;
    background:radial-gradient(ellipse at 40% 55%,var(--paper) 0%,var(--cream) 75%)}
  .flyer svg{position:absolute;inset:0;display:block}
  .intro{font-family:"Raleway",sans-serif;fill:var(--green)}
  .intro-small{font-size:26px;font-weight:500}
  .intro-big{font-size:60px;font-weight:800}
  .headline{font-family:"Elsie",serif;font-weight:900;fill:var(--purple)}
  .photo-label{font-family:"Raleway",sans-serif;font-weight:800;font-size:22px;fill:#fff}
  .badge-text{font-family:"Raleway",sans-serif;font-weight:800;fill:#fff;text-anchor:middle}
  .insured{font-family:"Raleway",sans-serif;font-weight:400;font-size:25px;fill:#fff;letter-spacing:3px}
  .brand-name{font-family:"Raleway",sans-serif;font-weight:600;font-size:30px;fill:var(--purple)}
  .company{font-family:"Raleway",sans-serif;font-weight:600;font-size:21px;fill:var(--ink)}
  .address{font-family:"Raleway",sans-serif;font-weight:400;font-size:19px;fill:var(--ink)}
  .phone{font-family:"Raleway",sans-serif;font-weight:500;font-size:36px;fill:var(--ink)}
  .web{font-family:"Raleway",sans-serif;font-weight:500;font-size:14px;fill:var(--ink);letter-spacing:1.6px}
</style>
</head>
<body>
<main class="flyer">
<svg viewBox="0 0 846 1200" width="846" height="1200">
  <defs>
    <linearGradient id="ring-green" x1="0" y1="0" x2="1" y2="1">
      <stop offset="0" stop-color="var(--green-dark)"/>
      <stop offset="1" stop-color="var(--green-light)"/>
    </linearGradient>
    <linearGradient id="ring-purple" x1="0" y1="0" x2="1" y2="1">
      <stop offset="0" stop-color="var(--purple)"/>
      <stop offset="1" stop-color="var(--purple-light)"/>
    </linearGradient>
    <radialGradient id="badge-green" cx="0.35" cy="0.3" r="0.8">
      <stop offset="0" stop-color="var(--green-light)"/>
      <stop offset="1" stop-color="var(--green-dark)"/>
    </radialGradient>
    <linearGradient id="photo-gutter" x1="0" y1="0" x2="1" y2="1">
      <stop offset="0" stop-color="#8f8a6a"/><stop offset="0.5" stop-color="#c9c6b6"/><stop offset="1" stop-color="#6f8a4a"/>
    </linearGradient>
    <linearGradient id="photo-blower" x1="0" y1="0" x2="1" y2="1">
      <stop offset="0" stop-color="#b46a52"/><stop offset="1" stop-color="#7a5a48"/>
    </linearGradient>
    <linearGradient id="photo-leaves" x1="0" y1="0" x2="1" y2="1">
      <stop offset="0" stop-color="#7e9a4a"/><stop offset="1" stop-color="#d9b45a"/>
    </linearGradient>
    <linearGradient id="photo-moss" x1="0" y1="0" x2="1" y2="1">
      <stop offset="0" stop-color="#e8eae4"/><stop offset="0.55" stop-color="#7d6a55"/><stop offset="1" stop-color="#8a8a86"/>
    </linearGradient>
    <path id="insured-arc" d="M 420 700 A 230 230 0 0 0 600 1000"/>
  </defs>

  <!-- background sweeps -->
  <g class="sweeps">
    <path d="M0,400 C50,690 240,930 580,965 L580,990 C220,965 30,770 0,480 Z" fill="var(--green)"/>
    <path d="M0,640 C120,830 320,885 520,880 L520,900 C300,908 100,865 0,705 Z" fill="var(--green-light)"/>
    <path d="M0,830 C150,935 360,975 560,975 L560,995 C340,998 130,960 0,880 Z" fill="var(--green-light)" opacity="0.85"/>
  </g>

  <!-- intro -->
  <text class="intro intro-small" x="37" y="68">We are</text>
  <text class="intro intro-big" x="36" y="124">offering</text>

  <!-- headline -->
  <g class="headline">
    <text x="140" y="246" font-size="100">A</text>
    <text x="76" y="316" font-size="126" textLength="364" lengthAdjust="spacingAndGlyphs">gutter</text>
    <text x="38" y="392" font-size="60" textLength="270" lengthAdjust="spacingAndGlyphs">clearance</text>
    <text x="118" y="448" font-size="62" textLength="230" lengthAdjust="spacingAndGlyphs">service</text>
    <text x="276" y="487" font-size="32">in</text>
    <text x="78" y="532" font-size="64" textLength="258" lengthAdjust="spacingAndGlyphs">swindon</text>
  </g>

  <!-- photo circles -->
  <g class="photo before-after">
    <circle cx="676" cy="190" r="154" fill="url(#ring-green)"/>
    <circle cx="666" cy="216" r="132" fill="url(#photo-gutter)" role="img" aria-label="Photo of a gutter before and after clearing"/>
    <text class="photo-label" x="603" y="154">Before</text>
    <text class="photo-label" x="714" y="253">After</text>
  </g>
  <g class="photo blower">
    <circle cx="494" cy="452" r="150" fill="url(#ring-green)"/>
    <circle cx="491" cy="472" r="126" fill="url(#photo-blower)" role="img" aria-label="Photo of a worker clearing a gutter with a vacuum pole"/>
  </g>
  <g class="photo leaves">
    <circle cx="722" cy="466" r="150" fill="url(#ring-purple)"/>
    <circle cx="716" cy="478" r="128" fill="url(#photo-leaves)" role="img" aria-label="Photo of gloved hands removing leaves from a gutter"/>
  </g>
  <g class="photo moss">
    <circle cx="640" cy="768" r="258" fill="url(#ring-purple)"/>
    <circle cx="660" cy="768" r="200" fill="url(#photo-moss)" role="img" aria-label="Close-up photo of moss and debris in a roof gutter"/>
    <text class="insured"><textPath href="#insured-arc">we are fully insured</textPath></text>
  </g>

  <!-- price badge -->
  <g class="price-badge">
    <circle cx="272" cy="684" r="104" fill="var(--silver)" stroke="#ffffff" stroke-width="4"/>
    <circle cx="272" cy="684" r="84" fill="url(#badge-green)"/>
    <text class="badge-text" x="272" y="632" font-size="15">PRICES</text>
    <text class="badge-text" x="272" y="652" font-size="15">START AT JUST</text>
    <text class="badge-text" x="272" y="708" font-size="60">£60</text>
    <text class="badge-text" x="272" y="728" font-size="11">FOR THE AVERAGE</text>
    <text class="badge-text" x="272" y="744" font-size="11">3 BED HOUSE</text>
  </g>

  <!-- brand -->
  <g class="brand">
    <circle cx="58" cy="990" r="18" fill="var(--green)"/>
    <text class="brand-name" x="86" y="1000">Marlow Treecare</text>
  </g>

  <!-- contact -->
  <g class="contact">
    <text class="company" x="37" y="1080">Marlow Treecare Services Ltd</text>
    <path d="M44,1097 a7,7 0 0 1 14,0 c0,6 -7,13 -7,13 c0,0 -7,-7 -7,-13 z" fill="none" stroke="var(--ink)" stroke-width="1.8"/>
    <circle cx="51" cy="1097" r="2.4" fill="var(--ink)"/>
    <text class="address" x="66" y="1112">Orbit Trading Centre</text>
    <text class="address" x="66" y="1135">Fairbrook Vale Ind Estate</text>
    <text class="address" x="66" y="1158">swindon SN4 7HW</text>

    <path d="M527,1094 c-3,2 -3,8 2,13 c5,5 11,6 13,3 l-3,-4 l-3,1 c-2,-1 -5,-4 -6,-6 l1,-3 z" fill="var(--ink)"/>
    <text class="phone" x="558" y="1110">01793 418302</text>
    <rect x="526" y="1126" width="13" height="9" fill="none" stroke="var(--ink)" stroke-width="1.4"/>
    <path d="M526,1126 l6.5,5 l6.5,-5" fill="none" stroke="var(--ink)" stroke-width="1.4"/>
    <text class="web" x="557" y="1135">dean@marlowtreecare.co.uk</text>
    <circle cx="532" cy="1154" r="7" fill="none" stroke="var(--ink)" stroke-width="1.4"/>
    <path d="M525,1154 h14 M532,1147 v14" stroke="var(--ink)" stroke-width="1"/>
    <text class="web" x="557" y="1159">www.marlowtreecare.co.uk</text>
  </g>
</svg>
</main>
</body>
</html>
```